K&R Security Services PTY. LTD.

Ive just had my logo made and I'm looking for some simple but strong designs for my business cards the company is a security company.

Please use dark colors.

Regards,

Owen Deloit

Reason: Need more time for discussion with other directors

Industry/Entity Type

Security

Font styles to use
Sans Serif
Decorative

```html
<!DOCTYPE html>
<html lang="en">
<head>
<meta charset="utf-8">
<title>K&amp;R Security Services – Business Card</title>
<link href="https://fonts.googleapis.com/css2?family=Open+Sans:wght@400;600&display=swap" rel="stylesheet">
<style>
  :root {
    --backdrop: #dcd9d4;
    --card: #878787;
    --band: #111111;
    --ink: #1e1e1e;
    --name: #e4e4e4;
    --band-text: #cfcfcf;
    --mark: #f2f2f2;
  }
  * { margin: 0; padding: 0; box-sizing: border-box; }
  html, body {
    width: 1200px; height: 1000px; overflow: hidden;
    background: var(--backdrop);
    font-family: "Open Sans", Arial, sans-serif;
  }
  .canvas { position: relative; width: 1200px; height: 1000px; }
  .card {
    position: absolute; width: 598px; height: 367px;
    background: var(--card);
    box-shadow: 0 4px 10px rgba(0,0,0,0.25);
    overflow: hidden;
  }
  .card--front { left: 185px; top: 110px; }
  .card--back { left: 387px; top: 516px; }

  .brand-mark {
    position: absolute; color: var(--mark);
    font-weight: 600; letter-spacing: 1px; line-height: 1;
  }
  .card--front .brand-mark { left: 55px; top: 110px; width: 130px; text-align: center; font-size: 44px; }

  .holder { position: absolute; left: 297px; top: 55px; width: 301px; }
  .holder__name { font-size: 24px; font-weight: 600; color: var(--name); line-height: 1.1; }
  .holder__role { font-size: 14px; color: var(--ink); margin-top: 2px; }
  .holder__rule { height: 1px; background: var(--ink); margin-top: 9px; }

  .contact { position: absolute; left: 297px; color: var(--ink); font-size: 14px; line-height: 17px; }
  .contact--address { top: 124px; }
  .contact--web { top: 147px; }
  .contact--phone { top: 191px; }
  .contact-row { display: flex; align-items: center; gap: 8px; }
  .contact-icon { width: 32px; height: 32px; flex: none; }

  .company-band {
    position: absolute; left: 0; top: 243px; width: 100%; height: 67px;
    background: var(--band);
    display: flex; align-items: center; justify-content: center;
    color: var(--band-text); font-size: 24px; font-weight: 600; letter-spacing: 2.4px;
    padding-left: 2px;
  }

  .back-band {
    position: absolute; left: 0; top: 164px; width: 100%; height: 58px;
    background: var(--band);
  }
  .card--back .brand-mark {
    left: 0; width: 100%; top: 164px; height: 58px;
    display: flex; align-items: center; justify-content: center;
    font-size: 44px;
  }
</style>
</head>
<body>
<div class="canvas">

  <section class="card card--front">
    <div class="brand-mark">K&amp;R</div>

    <div class="holder">
      <div class="holder__name">OWEN DELOIT</div>
      <div class="holder__role">Director</div>
      <div class="holder__rule"></div>
    </div>

    <div class="contact contact--address">P.O. Box 7 Ashgrove Victoria 3140</div>

    <div class="contact contact--web contact-row">
      <svg class="contact-icon" viewBox="0 0 32 32" aria-hidden="true">
        <circle cx="16" cy="16" r="16" fill="#1e1e1e"/>
        <g fill="none" stroke="#e0e0e0" stroke-width="1.3">
          <circle cx="16" cy="16" r="8"/>
          <ellipse cx="16" cy="16" rx="3.6" ry="8"/>
          <line x1="8" y1="16" x2="24" y2="16"/>
          <line x1="9.2" y1="12" x2="22.8" y2="12"/>
          <line x1="9.2" y1="20" x2="22.8" y2="20"/>
        </g>
      </svg>
      <div>owen@krsecure.net.au<br>krsecure.net.au</div>
    </div>

    <div class="contact contact--phone contact-row">
      <svg class="contact-icon" viewBox="0 0 32 32" aria-hidden="true">
        <circle cx="16" cy="16" r="16" fill="#1e1e1e"/>
        <path d="M11.5 8.5l2.6-.6 1.6 3.9-1.8 1.4c.9 2 2.4 3.5 4.4 4.4l1.4-1.8 3.9 1.6-.6 2.6c-.2.8-.9 1.3-1.7 1.2C15.5 20.8 11.2 16.5 10.8 10.7c0-.9.4-1.9.7-2.2z" fill="#e0e0e0"/>
      </svg>
      <div>0491570156<br>(03) 55500148</div>
    </div>

    <div class="company-band">K&amp;R SECURITY SERVICES PTY. LTD.</div>
  </section>

  <section class="card card--back">
    <div class="back-band"></div>
    <div class="brand-mark">K&amp;R</div>
  </section>

</div>
</body>
</html>
```